New Menu for Elegant Cafe Pastry Shop

We need to choose a design and layout for our new menu. We would like to also condense our current menu to 4-6 pages.
We will be changing prices and items on the menu, so it needs to be editable. Adobe formats are preferred. The size of the pages needs to be letter size. We will be printing it in house
Please take inspiration from the photos of our shop and food and also our Picmosaic page.
Attached are our current menu our logo and the logo info

https://www.picmosaic.com/marbrecoquette/?hl=en
https://maps.wayfindr.app/Qk3Lm9Xp2Tb7VwR4a

Industry/Entity Type

Food Cafe Bakery pastry

Other font styles liked:
• please look at attached files

Colors

Designer to choose colors to be used in the design.

Requirements
Nice to have
• Use of Arches like on our shop wallpaper or oblong eclair shapes, Art Deco elements

```html
<!DOCTYPE html>
<html lang="en">
<head>
<meta charset="utf-8">
<title>Marbre Coquette — Menu Pages</title>
<link rel="stylesheet" href="https://fonts.googleapis.com/css2?family=Kalam:wght@400;700&family=Libre+Baskerville:wght@700&family=Open+Sans:wght@400;600;700&display=swap">
<style>
  :root{
    --bg:#e6e2df;
    --paper:#f1efee;
    --rose:#b0686a;
    --rose-soft:#d9b8b8;
    --rose-pale:#ead8d8;
    --ink:#2f2b2b;
    --blue:#3b5fb0;
    --red:#d0453a;
    --green:#3e8a3e;
  }
  *{box-sizing:border-box;margin:0;padding:0}
  html,body{width:1200px;height:739px;overflow:hidden;background:var(--bg)}
  body{position:relative;font-family:"Open Sans",sans-serif;color:var(--ink)}
  .page{position:absolute;top:191px;width:276px;height:357px;background:var(--paper);
    box-shadow:0 2px 8px rgba(0,0,0,.18);padding:16px 18px}
  .page::before{content:"";position:absolute;inset:7px;border:1px dotted var(--rose)}
  .page::after{content:"";position:absolute;inset:10px;border:1px solid var(--rose-soft)}
  .page > *{position:relative;z-index:1}
  .p1{left:24px}.p2{left:316px}.p3{left:608px}.p4{left:900px}
  .corner{position:absolute;width:26px;height:26px;background:var(--rose-pale);z-index:1}
  .corner.tl{top:12px;left:12px}.corner.tr{top:12px;right:12px}
  .corner.bl{bottom:12px;left:12px}.corner.br{bottom:12px;right:12px}
  .brand{display:flex;align-items:center;justify-content:center;gap:4px;
    font-family:"Kalam",cursive;font-weight:700;color:var(--rose);font-size:9px;letter-spacing:.5px}
  .brand .dot{width:9px;height:9px;border-radius:50%;background:var(--rose)}
  .title{font-family:"Libre Baskerville",serif;font-weight:700;color:var(--rose);font-size:22px;line-height:1}
  .sub{font-family:"Libre Baskerville",serif;font-weight:700;font-size:5.5px;letter-spacing:.4px}
  .h{font-family:"Kalam",cursive;color:var(--rose);text-transform:uppercase;letter-spacing:.5px;line-height:1.1}
  .rule{height:1px;background:var(--rose);margin:5px auto;width:100px}
  .art{background:var(--rose-soft);border-radius:4px}
  .row{display:flex;justify-content:space-between}
  .legend{position:absolute;left:0;right:0;bottom:17px;text-align:center;font-size:3.4px;z-index:1}
  .legend .b{color:var(--blue)}.legend .r{color:var(--red)}.legend .g{color:var(--green)}

  /* page 1: fixed placement of each block */
  .p1 .abs{position:absolute;z-index:1}
  .p1 .brand-wrap{left:0;right:0;top:34px}
  .p1 .title-wrap{left:0;right:0;top:66px;text-align:center}
  .p1 .title-wrap .sub{display:block;margin:2px 0 0 60px}
  .p1 .cup{width:38px;height:32px}
  .p1 .cup.left{left:44px;top:110px}
  .p1 .cup.right{left:194px;top:110px}
  .p1 .soups{left:84px;width:108px;top:104px;text-align:center}
  .p1 .soups .h{font-size:12px}
  .p1 .soups .line{font-size:6px;margin-top:4px}
  .p1 .rule.r1{left:88px;width:100px;top:147px;margin:0}
  .p1 .opera-head{left:29px;top:162px;width:200px;display:flex;gap:6px;align-items:baseline}
  .p1 .opera-head .h{font-size:7px}
  .p1 .opera-head .price{font-size:6px;font-weight:600}
  .p1 .opera-text{left:29px;top:174px;width:104px;font-size:5.6px;line-height:1.3}
  .p1 .cakes-head{left:146px;top:184px;width:100px;font-size:8.5px}
  .p1 .cakes{left:138px;top:198px;width:104px;font-size:5.8px;line-height:1.5}
  .p1 .cupcake{left:38px;top:208px;width:42px;height:62px}
  .p1 .rule.r2{left:88px;width:100px;top:246px;margin:0}
  .p1 .baba{left:86px;width:110px;top:262px;text-align:center}
  .p1 .baba .h{font-size:8.5px}
  .p1 .baba small{display:block;font-family:"Kalam",cursive;font-size:4.5px;margin:-1px 0 0 30px}
  .p1 .baba-rows{left:72px;top:287px;width:112px;font-size:5.8px;line-height:1.7}
  .p1 .slice{left:202px;top:240px;width:40px;height:36px}

  /* page 2 */
  .p2 .h{font-size:8px}
  .p2 .center{text-align:center}
  .p2 .big{font-size:10px;color:var(--ink)}
  .p2 .cols3{display:grid;grid-template-columns:repeat(3,1fr);gap:6px;margin-top:5px;font-size:5px;text-align:center;line-height:1.3}
  .p2 .cols3 .h{font-size:6.5px}
  .p2 .cols2{display:grid;grid-template-columns:1fr 1fr;gap:12px;margin-top:4px}
  .p2 .cols2 .row{font-size:5.2px;line-height:1.55}
  .p2 .syr{font-size:5px;text-align:center;margin:2px 0 4px}

  /* page 3 */
  .p3{font-size:4.3px;line-height:1.3}
  .p3 .h{font-size:7px}
  .p3 .lunch{text-align:center;font-size:10px;color:var(--ink);margin-top:2px}
  .p3 .g2{display:grid;grid-template-columns:1fr 1fr;gap:10px}
  .p3 .g3{display:grid;grid-template-columns:1fr 1fr 1fr;gap:6px;margin-top:4px}
  .p3 b{font-weight:700;display:block;margin-top:3px}
  .p3 .sect{text-align:center;margin-top:4px}
  .p3 .sect .h{color:var(--ink);font-size:8px}
  .p3 .side{font-size:4.3px}

  /* page 4 */
  .p4 .flourish{height:44px;width:190px;margin:14px auto 0;background:var(--rose-soft)}
  .p4 .top{text-align:center;margin-top:10px}
  .p4 .title{font-size:28px;margin-top:6px}
  .p4 .sub{font-size:7px}
  .p4 .keys{margin:16px 0 0 44px;font-family:"Open Sans",sans-serif;font-size:9.5px;line-height:1.35;font-weight:600}
  .p4 .keys span{font-weight:700}
  .p4 .cup{position:absolute;width:42px;height:34px}
  .p4 .flourish2{position:absolute;left:40px;right:40px;bottom:28px;height:30px;background:var(--rose-soft)}
</style>
</head>
<body>

<!-- Seasonal page -->
<section class="page p1">
  <div class="corner tl" role="img" aria-label="corner flourish ornament"></div>
  <div class="corner tr" role="img" aria-label="corner flourish ornament"></div>
  <div class="corner bl" role="img" aria-label="corner flourish ornament"></div>
  <div class="corner br" role="img" aria-label="corner flourish ornament"></div>

  <div class="abs brand-wrap"><div class="brand"><span class="dot"></span>MARBRE COQUETTE</div></div>
  <div class="abs title-wrap">
    <div class="title">Seasonal</div>
    <span class="sub">Upon Availability</span>
  </div>

  <div class="abs cup left art" role="img" aria-label="steaming cup illustration"></div>
  <div class="abs soups">
    <div class="h">Soups</div>
    <div class="line">Lorraine &nbsp;&nbsp;| &nbsp;&nbsp;$ 6.00</div>
  </div>
  <div class="abs cup right art" role="img" aria-label="steaming cup illustration"></div>
  <div class="abs rule r1"></div>

  <div class="abs opera-head"><span class="h">Pistachio Raspberry Opera CN |</span><span class="price">$ 8.80</span></div>
  <p class="abs opera-text">Pistachio Joconde cake layered with Pistachio buttercream, chocolate ganache and raspberry gelee</p>

  <div class="abs h cakes-head">Travel Cakes V</div>
  <div class="abs cakes">
    <div class="row"><span>Banana pecancn</span><span>$ 6.00</span></div>
    <div class="row"><span>Banana walnutcn</span><span>$ 6.00</span></div>
    <div class="row"><span>Banana chocolate chips</span><span>$ 6.00</span></div>
    <div class="row"><span>Blueberry</span><span>$ 6.00</span></div>
  </div>
  <div class="abs cupcake art" role="img" aria-label="cupcake illustration"></div>
  <div class="abs rule r2"></div>

  <div class="abs baba">
    <div class="h">Baba au Rhum</div>
    <small>CONTAIN ALCOHOL</small>
  </div>
  <div class="abs baba-rows">
    <div class="row"><span>Chocolate / Hazelnut cocoa</span><span>$ 7.80</span></div>
    <div class="row"><span>Vanilla / orange / pineapple</span><span>$ 7.80</span></div>
  </div>
  <div class="abs slice art" role="img" aria-label="cake slice illustration"></div>

  <div class="legend"><span class="b">(CN)</span> - CONTAINS NUTS <span class="b">(CA)</span> - CONTAINS ALMONDS <span class="b">(CW)</span> - CONTAINS WALNUTS <span class="r">(GF)</span> - GLUTEN FREE <span class="g">(V)</span> - VEGAN</div>
</section>

<!-- Drinks page -->
<section class="page p2">
  <div class="corner tl" role="img" aria-label="corner flourish ornament"></div>
  <div class="corner tr" role="img" aria-label="corner flourish ornament"></div>
  <div class="corner bl" role="img" aria-label="corner flourish ornament"></div>
  <div class="corner br" role="img" aria-label="corner flourish ornament"></div>
  <div class="center h big" style="margin-top:6px">Mocktails</div>
  <div class="cols3">
    <div><div class="h">Pina Colada</div>A tropical classic mocktail of pineapple and coconut<br><b>$ 6.30</b></div>
    <div><div class="h">Mango Lychee</div>Refreshing mix of lychee and mango<br><b>$ 6.50</b></div>
    <div><div class="h">Ruby Fizz</div>Ginger ale and grenadine mocktail garnished with maraschino cherry.<br><b>$ 6.30</b></div>
  </div>
  <div class="rule"></div>
  <div class="center h big">Coffees &amp; Beverages</div>
  <div class="cols2">
    <div>
      <div class="h">Iced Coffee</div>
      <div class="row"><span>Iced espresso</span><span>$4.00</span></div>
      <div class="row"><span>Iced Cappuccino</span><span>$4.55</span></div>
      <div class="row"><span>Iced latte</span><span>$4.75</span></div>
    </div>
    <div>
      <div class="h">Hot Coffee</div>
      <div class="row"><span>French press</span><span>$3.80</span></div>
      <div class="row"><span>Espresso</span><span>$3.50</span></div>
      <div class="row"><span>Cappuccino</span><span>$4.25</span></div>
      <div class="row"><span>Latte</span><span>$4.50</span></div>
      <div class="row"><span>americano</span><span>$3.75</span></div>
    </div>
  </div>
  <div class="center h big">Syrups</div>
  <div class="syr">vanilla | hazelnut | caramel | mocha | dark or white chocolate sauce</div>
  <div class="h">Cold Drinks</div>
  <div class="cols2">
    <div>
      <div class="row"><span>Spring Water 16 oz</span><span>$3.70</span></div>
      <div class="row"><span>Sparkling mineral</span><span>$4.70</span></div>
      <div class="row"><span>Cola / diet</span><span>$4.00</span></div>
      <div class="row"><span>Bubbly water</span><span>$4.70</span></div>
      <div class="row"><span>Homemade Lemonade</span><span>$6.50</span></div>
      <div class="row"><span>Mint Lemonade</span><span>$6.50</span></div>
      <div class="row"><span>strawberry Lemonade</span><span>$6.50</span></div>
      <div class="row"><span>Lavender Lemonade</span><span>$6.50</span></div>
      <div class="row"><span>orange juice</span><span>$4.70</span></div>
    </div>
    <div>
      <div class="row"><span>Earl grey tea</span><span>$3.90</span></div>
      <div class="row"><span>Darjeeling tea</span><span>$3.90</span></div>
      <div class="row"><span>Ginger tea</span><span>$3.90</span></div>
      <div class="row"><span>Camomile tea</span><span>$3.90</span></div>
      <div class="row"><span>mint tea</span><span>$3.90</span></div>
      <div class="row"><span>fruit smoothie</span><span>$6.80</span></div>
      <div class="row"><span>iced tea</span><span>$4.20</span></div>
      <div class="row"><span>dragon fruit cooler</span><span>$6.50</span></div>
      <div class="row"><span>green tea latte</span><span>$5.20</span></div>
    </div>
  </div>
  <div class="legend"><span class="b">(CN)</span> - CONTAINS NUTS <span class="b">(CA)</span> - CONTAINS ALMONDS <span class="b">(CW)</span> - CONTAINS WALNUTS <span class="r">(GF)</span> - GLUTEN FREE <span class="g">(V)</span> - VEGAN</div>
</section>

<!-- Lunch page -->
<section class="page p3">
  <div class="corner tl" role="img" aria-label="corner flourish ornament"></div>
  <div class="corner tr" role="img" aria-label="corner flourish ornament"></div>
  <div class="corner bl" role="img" aria-label="corner flourish ornament"></div>
  <div class="corner br" role="img" aria-label="corner flourish ornament"></div>
  <div class="h lunch">Lunch</div>
  <div class="g2">
    <div>
      <div class="h">Salads</div>
      <b>Greek</b>Baby tomatoes, cucumbers, feta, olives, onions, P.O.V. olive oil, vinegar<br>$5.50
      <b>garden roquefort</b>Baby greens, arugula, beets, Roquefort P.O.V. blue cheese, caramelized pistachios, strawberries, orange vinaigrette<br>$5.50
      <b>Zucchini</b>Fresh spiralized zucchini with feta, mint, almonds, lemon, POV olive oil<br>$6.55
    </div>
    <div>
      <div class="h">Soups</div>
      <b>French Onion Soup</b>Classic onion soup gratinated with gruyere cheese and crunchy eclairs<br>$7.95
      <b>Pumpkin Soup</b>Homemade pumpkin soup served with cream and crushed chickpeas<br>$6.60
      <b>tomato Soup</b>Tomato soup served with prosciutto gruyere cheese and crunchy eclairs<br>$7.60
    </div>
  </div>
  <div class="g3">
    <div><div class="h">Quiches</div>available also in GF crust<br>Lorraine<br>Mushroom<br>Spinach<br>Salmon tomato<br>$6.99</div>
    <div><div class="h">Phyllo Pocket</div>Feta cheese served hot drizzled with honey and sesame<br>$4.60</div>
    <div><div class="h">Brioches</div>Ham and cheese<br>Feta and thyme<br>$4.30</div>
  </div>
  <div class="sect"><div class="h">Savory Eclairs</div><div class="side">Side of green salad +$3.50</div></div>
  <div class="g2">
    <div>
      <div class="h" style="text-align:center">Cold</div>
      <b>Tuna Salad Éclair</b>Classic tuna salad with refreshing grapes and celery.<br>$7.55
      <b>Caprese Éclair</b>Roquefort cream, Prosciutto, glazed pear wedges, caramelized pistachios, fig glaze<br>$9.75
      <b>Roquefort Dream Éclair (CN)</b>Fresh spiralized zucchini with feta, mint, almonds, lemon<br>$6.55
      <b>Shepherd's pie Éclair</b>Whipped cream cheese with chives, smoked salmon, dill<br>$9.75
    </div>
    <div>
      <div class="h" style="text-align:center">Hot</div>
      <b>Shepherd's pie Éclair</b>Seasoned ground beef, topped with creamy mashed potatoes, grated Parmesan<br>$9.55
      <b>Chicken, Spinach, Artichoke Éclair</b>Rich cream with spinach chicken and artichoke hearts, gouda cheese<br>$9.75
      <b>Mushroom Éclair</b>Creamy mashed potatoes, sautéed mushrooms, Parmesan, truffle oil<br>$9.75
      <b>Sweet brie Éclair</b>Melted brie, arugula, strawberry sauce and fresh strawberry halves<br>$9.75
    </div>
  </div>
  <div class="legend"><span class="b">(CN)</span> - CONTAINS NUTS <span class="b">(CA)</span> - CONTAINS ALMONDS <span class="b">(CW)</span> - CONTAINS WALNUTS <span class="r">(GF)</span> - GLUTEN FREE <span class="g">(V)</span> - VEGAN</div>
</section>

<!-- Cover page -->
<section class="page p4">
  <div class="corner tl" role="img" aria-label="corner flourish ornament"></div>
  <div class="corner tr" role="img" aria-label="corner flourish ornament"></div>
  <div class="corner bl" role="img" aria-label="corner flourish ornament"></div>
  <div class="corner br" role="img" aria-label="corner flourish ornament"></div>
  <div class="flourish art" role="img" aria-label="large scroll flourish ornament"></div>
  <div class="top">
    <div class="brand"><span class="dot"></span>MARBRE COQUETTE</div>
    <div class="title">Seasonal</div>
    <div class="sub" style="margin-left:70px">Upon Availability</div>
  </div>
  <div class="keys">
    <div><span>(CN)</span> - CONTAINS NUTS</div>
    <div><span>(CA)</span> - CONTAINS ALMONDS</div>
    <div><span>(CW)</span> - CONTAINS WALNUTS</div>
    <div><span>(GF)</span> - GLUTEN FREE</div>
    <div><span>(V)</span> - VEGAN</div>
  </div>
  <div class="cup art" style="left:22px;top:250px" role="img" aria-label="coffee cup illustration"></div>
  <div class="cup art" style="right:26px;top:262px" role="img" aria-label="coffee cup illustration"></div>
  <div class="flourish2 art" role="img" aria-label="bottom scroll flourish ornament"></div>
</section>

</body>
</html>
```